Real Estate Business Cards

Looking for a clean, sharp and professional look for our Real Estate investment Fund that invests in Multi Family Apartment buildings.

Target Market(s)

Real Estate Fund

Industry/Entity Type

Real Estate

Contact Information for Business Card

Company Description: Real Estate Investment Fund
Company Name: RKW Holdings
Name: Marcus Olvane
Cell: (917) 482-0657
Email: marcus@rkwholdings-example.com
Website: www.rkwholdings-example.com
Address: 418, 9th Street, Brooklyn NY 11218

Colors

Designer to choose colors to be used in the design.

Requirements
Nice to have
• Colors to match logo

```html
<!DOCTYPE html>
<html lang="en">
<head>
<meta charset="utf-8">
<title>RKW Holdings — Business Cards</title>
<link href="https://fonts.googleapis.com/css2?family=Montserrat:wght@600&family=Roboto:wght@300;400&display=swap" rel="stylesheet">
<style>
  :root {
    --backdrop: #d4d4d4;
    --brand-blue: #0d72ab;
    --blue-1: #00a0e3;
    --blue-2: #0093d8;
    --blue-3: #0087cf;
    --charcoal: #4b4b4b;
    --grey-1: #5a5a5a;
    --grey-2: #7b7b7b;
    --grey-3: #b3b3b3;
    --row-1: #5a5a5a;
    --row-1-icon: #575757;
    --row-2: #8e8e8e;
    --row-2-icon: #7f7f7f;
    --row-3: #c9c9c9;
    --row-3-icon: #b5b5b5;
    --row-4: #e1e1e1;
    --row-4-icon: #cdcdcd;
    --white: #ffffff;
  }
  * { box-sizing: border-box; margin: 0; padding: 0; }
  html, body { width: 1200px; height: 1200px; overflow: hidden; }
  body { background: var(--backdrop); position: relative; font-family: "Roboto", Arial, sans-serif; color: var(--white); }

  .card { position: absolute; left: 184px; width: 833px; overflow: hidden; }
  .card--front { top: 107px; height: 469px; background: var(--brand-blue); }
  .card--back { top: 624px; height: 472px; background: var(--charcoal); }

  .tile-stack { position: absolute; width: 56px; }
  .tile-stack span { display: block; height: 56px; }
  .tile-stack--front-top { left: 0; top: 0; }
  .tile-stack--front-top span:nth-child(1) { background: var(--blue-1); }
  .tile-stack--front-top span:nth-child(2) { background: var(--blue-2); }
  .tile-stack--front-top span:nth-child(3) { background: var(--blue-3); }
  .tile-stack--front-bottom { right: 0; bottom: 0; }
  .tile-stack--front-bottom span:nth-child(1) { background: var(--blue-3); }
  .tile-stack--front-bottom span:nth-child(2) { background: var(--blue-2); }
  .tile-stack--front-bottom span:nth-child(3) { background: var(--blue-1); }
  .tile-stack--back { left: 0; top: 0; }
  .tile-stack--back span:nth-child(1) { background: var(--grey-1); }
  .tile-stack--back span:nth-child(2) { background: var(--grey-2); }
  .tile-stack--back span:nth-child(3) { background: var(--grey-3); }

  .brand { position: absolute; display: flex; align-items: center; }
  .brand__mark { background: var(--white); flex: none; }
  .brand__name { font-family: "Roboto", Arial, sans-serif; font-weight: 300; text-transform: uppercase; color: var(--white); white-space: nowrap; }

  .card--front .brand { left: 0; right: 0; top: 150px; flex-direction: column; }
  .card--front .brand__mark { width: 92px; height: 92px; margin-bottom: 36px; }
  .card--front .brand__name { font-size: 50px; letter-spacing: 4px; }

  .tagline { position: absolute; left: 441px; top: 371px; font-size: 20px; letter-spacing: 1.4px; font-weight: 400; }

  .card--back .brand { left: 120px; top: 92px; }
  .card--back .brand__mark { width: 104px; height: 104px; margin-right: 32px; }
  .card--back .brand__name { font-size: 44px; letter-spacing: 3px; }

  .person { position: absolute; right: 539px; top: 264px; text-align: right; }
  .person__row { display: flex; align-items: center; justify-content: flex-end; gap: 14px; }
  .person__icon { width: 22px; height: 22px; flex: none; }
  .person__name { font-family: "Montserrat", Arial, sans-serif; font-weight: 600; font-size: 22px; letter-spacing: 0.8px; white-space: nowrap; }
  .person__company { font-size: 17px; font-weight: 300; margin-top: 6px; white-space: nowrap; }
  .person__rule { width: 59px; height: 4px; background: var(--white); margin: 10px 0 0 auto; }

  .contact-list { position: absolute; left: 417px; top: 215px; width: 390px; list-style: none; }
  .contact-list li { display: flex; height: 57px; }
  .contact-list .contact__text { flex: 1; display: flex; align-items: center; justify-content: center; text-align: center; font-size: 17px; letter-spacing: 1.2px; line-height: 1.2; white-space: nowrap; }
  .contact-list .contact__icon { width: 82px; display: flex; align-items: center; justify-content: center; }
  .contact-list svg { width: 24px; height: 24px; fill: var(--white); }
  .contact--phone .contact__text { background: var(--row-1); }
  .contact--phone .contact__icon { background: var(--row-1-icon); }
  .contact--email .contact__text { background: var(--row-2); font-size: 16px; letter-spacing: 0.6px; }
  .contact--email .contact__icon { background: var(--row-2-icon); }
  .contact--address .contact__text { background: var(--row-3); }
  .contact--address .contact__icon { background: var(--row-3-icon); }
  .contact--web .contact__text { background: var(--row-4); font-size: 16px; letter-spacing: 0.8px; }
  .contact--web .contact__icon { background: var(--row-4-icon); }
</style>
</head>
<body>

<section class="card card--front" aria-label="Card front">
  <div class="tile-stack tile-stack--front-top"><span></span><span></span><span></span></div>
  <div class="tile-stack tile-stack--front-bottom"><span></span><span></span><span></span></div>
  <div class="brand">
    <div class="brand__mark"></div>
    <div class="brand__name">RKW Holdings</div>
  </div>
  <p class="tagline">Real Estate Investment Fund</p>
</section>

<section class="card card--back" aria-label="Card back">
  <div class="tile-stack tile-stack--back"><span></span><span></span><span></span></div>
  <div class="brand">
    <div class="brand__mark"></div>
    <div class="brand__name">RKW Holdings</div>
  </div>

  <div class="person">
    <div class="person__row">
      <svg class="person__icon" viewBox="0 0 24 24" fill="#fff" aria-hidden="true">
        <circle cx="12" cy="7" r="5.5"/>
        <path d="M1 24c0-6 4.5-10 11-10s11 4 11 10z"/>
      </svg>
      <div class="person__name">Marcus Olvane</div>
    </div>
    <div class="person__company">RKW Holdings</div>
    <div class="person__rule"></div>
  </div>

  <ul class="contact-list">
    <li class="contact--phone">
      <span class="contact__text">(917) 482-0657</span>
      <span class="contact__icon"><svg viewBox="0 0 24 24" aria-hidden="true"><path d="M6.6 10.8a15.1 15.1 0 0 0 6.6 6.6l2.2-2.2c.3-.3.7-.4 1-.2 1.1.4 2.3.6 3.6.6.6 0 1 .4 1 1V20c0 .6-.4 1-1 1A17 17 0 0 1 3 4c0-.6.4-1 1-1h3.5c.6 0 1 .4 1 1 0 1.3.2 2.5.6 3.6.1.3 0 .7-.2 1z"/></svg></span>
    </li>
    <li class="contact--email">
      <span class="contact__text">marcus@rkwholdings-example.com</span>
      <span class="contact__icon"><svg viewBox="0 0 24 24" aria-hidden="true"><path d="M2 5h20v1.5l-10 6.5L2 6.5z"/><path d="M2 9l10 6.5L22 9v10H2z"/></svg></span>
    </li>
    <li class="contact--address">
      <span class="contact__text">418, 9th Street,<br>Brooklyn NY 11218</span>
      <span class="contact__icon"><svg viewBox="0 0 24 24" aria-hidden="true"><path d="M12 2 1 11h3v11h16V11h3zm0 6a4 4 0 0 1 4 4c0 3-4 7-4 7s-4-4-4-7a4 4 0 0 1 4-4zm0 2.5a1.5 1.5 0 1 0 0 3 1.5 1.5 0 0 0 0-3z"/></svg></span>
    </li>
    <li class="contact--web">
      <span class="contact__text">www.rkwholdings-example.com</span>
      <span class="contact__icon"><svg viewBox="0 0 24 24" aria-hidden="true"><path d="M12 2a10 10 0 1 0 0 20 10 10 0 0 0 0-20zm-1 2.1V8H7.6A8 8 0 0 1 11 4.1zm2 0A8 8 0 0 1 16.4 8H13zM5.1 10H11v4H5.1a8 8 0 0 1 0-4zM13 10h5.9a8 8 0 0 1 0 4H13zm-5.4 6H11v3.9A8 8 0 0 1 7.6 16zm5.4 0h3.4a8 8 0 0 1-3.4 3.9z"/></svg></span>
    </li>
  </ul>
</section>

</body>
</html>
```